Schriftdesign für Shop-Header Bild (Schmuckhandel) / Online-Marketing Material
Zielgruppe
Wir verkaufen Schmuck im Onlineshop mit Herz
Aufgabenstellung
Wir benötigen den vorgegebenen Text in schöner Form, Farbe und Größe harmonisch eingefügt, in unserem Bild.
Folgender Text soll sich schick ins Bild einfügen oder in 3-D vielleicht in Schriftfarbe gold hervorheben:
Mit ganzem Herzen für Sie da!
Ihr Online -Juwelier mit Herz
Siehe auch unser altes Bild mit Text, im Shop, wie es nicht aussehen sollte: www.lindenglanzhof.de

```html
<!DOCTYPE html>
<html lang="de">
<head>
<meta charset="utf-8">
<title>Lindenglanzhof – Startseite</title>
<link href="https://fonts.googleapis.com/css2?family=Lato:wght@400;700&family=Quicksand:wght@500&family=Great+Vibes&family=Handlee&display=swap" rel="stylesheet">
<style>
:root{
  --red:#d6101c;
  --text:#222;
  --muted:#6b6b6b;
  --nav:#646264;
  --field:#efefef;
  --gold:#d9a531;
  --gold-dark:#8a5a12;
  --dot:#c9c9c9;
}
*{margin:0;padding:0;box-sizing:border-box}
html,body{width:1200px;height:855px;overflow:hidden;background:#fff;font-family:'Lato',sans-serif;color:var(--text)}
.page{position:relative;width:1200px;height:855px;overflow:hidden}

.brand{position:absolute;left:230px;top:40px;display:flex;align-items:center;gap:6px}
.brand-dot{width:14px;height:14px;border-radius:50%;background:var(--red)}
.brand-name{font-size:17px;font-weight:700;color:var(--red)}

.top-links{position:absolute;right:230px;top:7px;display:flex;gap:15px;font-size:9.5px}
.top-links a{color:var(--text);text-decoration:none}
.top-links a.active{color:var(--red)}

.search-label{position:absolute;left:421px;top:25px;font-size:13px;color:#111}
.search-label .caret{display:inline-block;border:5px solid transparent;border-top:6px solid var(--red);margin-left:6px;vertical-align:-3px}
.search{position:absolute;left:421px;top:47px;width:319px;height:30px;background:var(--field);font-size:10.5px;color:#777;padding:9px 18px}
.search svg,.cart svg{position:absolute;right:12px;top:6px}
.cart{position:absolute;left:783px;top:48px;width:187px;height:30px;background:var(--field);font-size:10.5px;color:#e8605f;padding:9px 19px}

.nav{position:absolute;left:0;top:104px;width:1200px;height:33px;background:var(--nav)}
.nav ul{list-style:none;display:flex;gap:30px;position:absolute;left:324px;top:9px}
.nav li{font-family:'Quicksand',sans-serif;font-size:12.5px;color:#fff;letter-spacing:.2px}
.nav-notch{position:absolute;left:248px;top:103px}

.hero{position:absolute;left:0;top:137px;width:1200px;height:298px;
  background:radial-gradient(ellipse at 58% 30%,#f6efe6 0%,#e9dccd 45%,#d8c5b2 100%)}
.hero-line{position:absolute;font-family:'Great Vibes',cursive;color:var(--gold);
  text-shadow:1px 1px 0 var(--gold-dark),2px 3px 4px rgba(90,50,10,.45);white-space:nowrap}
.hero-line.one{left:246px;top:140px;font-size:64px}
.hero-line.two{left:342px;top:210px;font-size:64px}
.hero-fade{position:absolute;left:0;top:435px;width:1200px;height:20px;background:linear-gradient(#e9e2dc,#fff)}

.badge{position:absolute;left:739px;top:461px}
.dots{position:absolute;left:727px;width:243px;border-top:3px dotted var(--dot)}
.dots.upper{top:535px}
.dots.lower{top:686px}
.promises{position:absolute;left:730px;top:558px;list-style:none}
.promises li{display:flex;align-items:center;gap:8px;height:30px;font-size:13px;color:var(--red)}

.store-note{position:absolute;left:230px;top:536px;font-size:14.5px;color:var(--muted)}
.store-note small{font-size:12px;color:#444}
.store-banner{position:absolute;left:230px;top:569px;width:466px;height:156px;box-shadow:0 0 3px rgba(0,0,0,.35);
  background:linear-gradient(90deg,#1d1d1d 0%,#2e2e2e 50%,#6a4a2a 70%,#3a3a3a 100%);overflow:hidden}
.store-name{position:absolute;left:12px;top:10px;font-family:'Lato',sans-serif;font-size:34px;color:#b49a5a;letter-spacing:1px}
.store-tag{position:absolute;left:3px;top:81px;width:173px;height:72px;background:#fff}
.store-pager{position:absolute;right:20px;bottom:10px;display:flex;gap:7px}
.store-pager span{width:8px;height:8px;border-radius:50%;background:#fff}
.store-pager span.on{background:var(--red)}

.welcome{position:absolute;left:230px;top:772px;font-family:'Handlee',cursive;font-size:20px;color:#555}
.welcome em{font-style:normal;color:var(--red)}
.welcome-sub{position:absolute;left:230px;top:818px;font-size:15px;font-weight:700;color:var(--muted)}
</style>
</head>
<body>
<div class="page">

  <div class="brand"><span class="brand-dot"></span><span class="brand-name">Lindenglanzhof</span></div>

  <nav class="top-links">
    <a class="active" href="#">Startseite</a><a href="#">Anmelden</a><a href="#">Mein Konto</a><a href="#">Newsletter abonnieren</a><a href="#">Kontakt</a>
  </nav>

  <div class="search-label">Nach welchem Artikel suchen Sie?<span class="caret"></span></div>
  <div class="search">Suchen nach
    <svg width="22" height="18" viewBox="0 0 22 18"><path d="M11 17C4 12 1 9 1 5.5A4.5 4.5 0 0 1 11 3a4.5 4.5 0 0 1 10 2.5C21 9 18 12 11 17Z" fill="#d6101c"/><circle cx="10.5" cy="7.5" r="2.5" fill="none" stroke="#fff" stroke-width="1.3"/><line x1="12.3" y1="9.3" x2="14" y2="11" stroke="#fff" stroke-width="1.3"/></svg>
  </div>
  <div class="cart">Ihr Warenkorb ist leer.
    <svg width="16" height="19" viewBox="0 0 16 19"><path d="M5 6V4a3 3 0 0 1 6 0v2" fill="none" stroke="#d6101c" stroke-width="1.5"/><rect x="0" y="6" width="16" height="13" rx="1" fill="#d6101c"/></svg>
  </div>

  <div class="nav"><ul><li>KREUZ-ANHÄNGER</li><li>ANHÄNGER/VERSCH.</li><li>FOTO-MEDAILLONS</li><li>OHRSCHMUCK</li><li>ACCESSOIRES</li></ul></div>
  <svg class="nav-notch" width="66" height="24" viewBox="0 0 66 24"><path d="M0 0H66L33 24Z" fill="#fff"/></svg>

  <section class="hero" role="img" aria-label="Goldener Herzanhänger an einer Kette auf cremefarbener, fließender Seide">
    <div class="hero-line one">Mit ganzem Herzen für Sie da!</div>
    <div class="hero-line two">Ihr Online -Juwelier mit Herz</div>
  </section>
  <div class="hero-fade"></div>

  <svg class="badge" width="110" height="68" viewBox="0 0 110 68" aria-hidden="true"><rect x="50" y="20" width="58" height="26" fill="#e8cc6a"/><circle cx="33" cy="33" r="33" fill="#1f3a7a"/><circle cx="33" cy="33" r="20" fill="#d9a531"/></svg>
  <div class="dots upper"></div>
  <ul class="promises">
    <li><svg width="26" height="22" viewBox="0 0 26 22"><path d="M13 21C5 15 1 11 1 6.5A5.5 5.5 0 0 1 13 4a5.5 5.5 0 0 1 12 2.5C25 11 21 15 13 21Z" fill="#f7c6cf" stroke="#e05a6e"/></svg>Versand innerhalb von 24 Stunden</li>
    <li><svg width="26" height="22" viewBox="0 0 26 22"><path d="M13 21C5 15 1 11 1 6.5A5.5 5.5 0 0 1 13 4a5.5 5.5 0 0 1 12 2.5C25 11 21 15 13 21Z" fill="#f7c6cf" stroke="#e05a6e"/></svg>schneller, persönlicher Service</li>
    <li><svg width="26" height="22" viewBox="0 0 26 22"><path d="M13 21C5 15 1 11 1 6.5A5.5 5.5 0 0 1 13 4a5.5 5.5 0 0 1 12 2.5C25 11 21 15 13 21Z" fill="#f7c6cf" stroke="#e05a6e"/></svg>Kundenzufriedenheit an erster Stelle</li>
    <li><svg width="26" height="22" viewBox="0 0 26 22"><path d="M13 21C5 15 1 11 1 6.5A5.5 5.5 0 0 1 13 4a5.5 5.5 0 0 1 12 2.5C25 11 21 15 13 21Z" fill="#f7c6cf" stroke="#e05a6e"/></svg>sichere Zahlungsmethoden</li>
  </ul>
  <div class="dots lower"></div>

  <p class="store-note">Besuchen Sie auch unseren AURELVAN-Schmuck Store: <small>hier</small></p>
  <div class="store-banner" role="img" aria-label="Goldschmelze in einer Werkstatt mit Flammen, Schmuckmarke Made in Germany">
    <div class="store-name">AURELVAN</div>
    <div class="store-tag"></div>
    <div class="store-pager"><span></span><span></span><span class="on"></span><span></span><span></span><span></span></div>
  </div>

  <h1 class="welcome">Herzlich Willkommen im <em>Lindenglanzhof.de</em> Schmuck-Shop</h1>
  <p class="welcome-sub">Ihr Online-Juwelier mit Herz</p>

</div>
</body>
</html>
```